Letterhead for small civil engineer company

We need bold and modern design for company letterhead in MS word. It needs to have company logo and company info. Somewhere in the upper right part of document needs to be space for "recever" and the documents starts with, example, "SUBJECT: CIVIL ENGINEER LETTERHEAD".

in the bottom part of document needs to be signature and date.

Company info: Veltrana d.o.o., Lipovac 15, Lipovac (Općina Brdarić), OIB 47396028154, www.veltrana.hr, info@veltrana.hr

Email of document sender needs to be somewhere if document, exapmle xyz@veltrana.hr

Target Market(s)

Civil engineer company and projects

Industry/Entity Type

Civil engineer

Font styles to use
Serif

Colors
F0912C
F2A743
F7CA91
FBE8D2
FDF5EE

Requirements
Must have
• Company logo and company info
Nice to have
• Moder and clean design
Should not have
• Too much details

```html
<!DOCTYPE html>
<html lang="hr">
<head>
<meta charset="utf-8">
<title>Veltrana d.o.o. – letterhead footer</title>
<link rel="stylesheet" href="https://fonts.googleapis.com/css2?family=Outfit:wght@300;400;700&display=swap">
<style>
  :root {
    --ink: #111111;
    --band: #666666;
    --accent: #E8943A;
    --paper: #ffffff;
    --on-band: #ffffff;
  }
  * { margin: 0; padding: 0; box-sizing: border-box; }
  html, body {
    width: 1200px;
    height: 271px;
    overflow: hidden;
    background: var(--paper);
  }
  .letterhead-footer {
    position: relative;
    width: 1200px;
    height: 271px;
    font-family: "Outfit", sans-serif;
    color: var(--ink);
  }
  .sign-field {
    position: absolute;
    left: 120px;
    display: flex;
    align-items: flex-end;
  }
  .sign-field--signature { top: 0; }
  .sign-field--date { top: 30px; }
  .sign-field__label {
    width: 121px;
    font-size: 21px;
    font-weight: 300;
    letter-spacing: 0.03em;
    line-height: 26px;
  }
  .sign-field__line {
    width: 156px;
    border-bottom: 2px solid var(--ink);
    margin-bottom: 1px;
  }
  .company-band {
    position: absolute;
    top: 138px;
    left: 0;
    width: 1200px;
    height: 26px;
    background: var(--band);
    color: var(--on-band);
    text-align: center;
    font-weight: 700;
    font-size: 21px;
    line-height: 28px;
    letter-spacing: 0.04em;
  }
  .contact-row {
    position: absolute;
    top: 186px;
    left: 120px;
    display: flex;
    align-items: center;
    gap: 14px;
  }
  .contact-item {
    display: flex;
    align-items: center;
    gap: 9px;
    font-size: 19px;
    font-weight: 300;
    letter-spacing: 0.04em;
    white-space: nowrap;
  }
  .contact-item__icon {
    width: 35px;
    height: 35px;
    flex: none;
  }
</style>
</head>
<body>
  <div class="letterhead-footer">
    <div class="sign-field sign-field--signature">
      <span class="sign-field__label">Signature:</span>
      <span class="sign-field__line"></span>
    </div>
    <div class="sign-field sign-field--date">
      <span class="sign-field__label">Date:</span>
      <span class="sign-field__line"></span>
    </div>

    <div class="company-band">Veltrana d.o.o.</div>

    <div class="contact-row">
      <div class="contact-item">
        <svg class="contact-item__icon" viewBox="0 0 36 36" aria-hidden="true">
          <circle cx="18" cy="18" r="18" fill="var(--accent)"/>
          <circle cx="18" cy="17" r="9.5" fill="none" stroke="#fff" stroke-width="1.6"/>
          <circle cx="18" cy="14.5" r="3.2" fill="#fff"/>
          <path d="M12.5 23.5 Q18 17.5 23.5 23.5 L18 28 Z" fill="#fff"/>
        </svg>
        <span>Lipovac 15, Lipovac (Općina Brdarić), OIB 47396028154</span>
      </div>
      <div class="contact-item">
        <svg class="contact-item__icon" viewBox="0 0 36 36" aria-hidden="true">
          <circle cx="18" cy="18" r="18" fill="var(--accent)"/>
          <rect x="6" y="11" width="24" height="15" fill="none" stroke="#fff" stroke-width="1.6"/>
          <path d="M6 11 L18 20 L30 11 M6 26 L14.5 17.5 M30 26 L21.5 17.5" fill="none" stroke="#fff" stroke-width="1.4"/>
        </svg>
        <span>info@veltrana.hr</span>
      </div>
      <div class="contact-item">
        <svg class="contact-item__icon" viewBox="0 0 36 36" aria-hidden="true">
          <circle cx="18" cy="18" r="18" fill="var(--accent)"/>
          <g fill="none" stroke="#fff" stroke-width="1.4">
            <circle cx="18" cy="18" r="11"/>
            <ellipse cx="18" cy="18" rx="5" ry="11"/>
            <line x1="18" y1="7" x2="18" y2="29"/>
            <line x1="7" y1="18" x2="29" y2="18"/>
            <line x1="9" y1="12.5" x2="27" y2="12.5"/>
            <line x1="9" y1="23.5" x2="27" y2="23.5"/>
          </g>
        </svg>
        <span>www.veltrana.hr</span>
      </div>
    </div>
  </div>
</body>
</html>
```